TALVERNE INSULATION STATIONARY
BUSINESS CARDS,STATIONARY,ENVELOPES & T-SHIRTS
Modern
ED TALVERNE
OWNER,SALES
14 BRISTLECONE CT. MARROWDALE,CA. 95000
TALVERNEINSULATION@MAILNEST.EXAMPLE
WWW.TALVERNEINSULATION.EXAMPLE
I'M GOING TO GET A WEBSITE DESIGN HERE TOO,THATS WHY I'M USING THE WEBSITE ADDRESS,PROBABLY MY E-MAIL IS GOING TO CHANGE AFTER I GET THE WEBSITE,BUT I THINK THIS IS EASY TO CHANGE.

```html
<!DOCTYPE html>
<html lang="en">
<head>
<meta charset="utf-8">
<title>Talverne Insulation – Stationery &amp; T-Shirt</title>
<link href="https://fonts.googleapis.com/css2?family=Jura:wght@400;600&display=swap" rel="stylesheet">
<style>
  :root{
    --bg:#050505;
    --paper:#ffffff;
    --green:#6dbd2b;
    --green-dark:#3d8c18;
    --green-light:#b9e27c;
    --green-pale:#e4f3cf;
    --ink:#4a4a4a;
    --white:#ffffff;
  }
  *{box-sizing:border-box;margin:0;padding:0}
  html,body{width:1200px;height:869px;overflow:hidden;background:var(--bg)}
  body{position:relative;font-family:"Jura",sans-serif;color:var(--ink)}

  /* brand lockup */
  .brand{display:flex;align-items:center;gap:8px;font-weight:600;color:var(--green);line-height:1;letter-spacing:.04em;text-transform:uppercase}
  .brand-mark{background:var(--green);flex:none}
  .brand-name{display:flex;flex-direction:column;gap:3px}

  /* t-shirt print */
  .shirt-print{position:absolute;left:60px;top:370px}
  .shirt-print .brand{gap:14px;font-size:34px}
  .shirt-print .brand-mark{width:56px;height:56px}
  .shirt-print .brand-name span+span{font-size:22px;letter-spacing:.12em}

  /* contact block */
  .contact{display:grid;grid-template-columns:36px auto;font-size:8.5px;line-height:1.55;color:var(--ink);white-space:nowrap}

  /* letterhead */
  .letterhead{position:absolute;left:420px;top:24px;width:360px;height:509px;background:var(--paper);overflow:hidden}
  .letterhead .band{position:absolute;top:0;bottom:0}
  .lh-band-1{left:0;width:14px;background:var(--green-dark)}
  .lh-band-2{left:14px;width:10px;background:var(--green)}
  .lh-band-3{left:24px;width:6px;background:var(--green-light)}
  .letterhead .brand{position:absolute;left:46px;top:26px;font-size:20px}
  .letterhead .brand-mark{width:30px;height:30px}
  .letterhead .brand-name span+span{font-size:13px;letter-spacing:.1em}
  .letterhead .contact{position:absolute;left:46px;top:74px}

  /* envelope */
  .envelope{position:absolute;left:810px;top:40px;width:360px;height:200px;background:var(--paper);overflow:hidden}
  .env-band-top{position:absolute;left:0;right:0;top:0;height:10px;background:var(--green)}
  .env-band-top-2{position:absolute;left:0;right:0;top:10px;height:5px;background:var(--green-light)}
  .envelope .brand{position:absolute;left:20px;top:32px;font-size:17px}
  .envelope .brand-mark{width:26px;height:26px}
  .envelope .brand-name span+span{font-size:11px;letter-spacing:.1em}
  .envelope .address{position:absolute;left:20px;top:88px;font-size:8px;line-height:1.5;text-transform:uppercase}
  .envelope .contact{position:absolute;left:20px;top:120px;font-size:8px}
  .env-decor{position:absolute;right:-20px;bottom:-30px;width:150px;height:170px;background:linear-gradient(135deg,var(--green-pale),#f4faea)}

  /* business cards */
  .card{position:absolute;left:810px;width:360px;height:206px;overflow:hidden}
  .card-front{top:292px;background:var(--paper)}
  .card-front .strip{position:absolute;left:0;top:0;bottom:0;width:12px;background:var(--green)}
  .card-front .strip-2{position:absolute;left:12px;top:0;bottom:0;width:5px;background:var(--green-light)}
  .card-front .brand{position:absolute;left:34px;top:24px;font-size:17px}
  .card-front .brand-mark{width:26px;height:26px}
  .card-front .brand-name span+span{font-size:11px;letter-spacing:.1em}
  .card-front .address{position:absolute;left:34px;top:86px;font-size:8px;line-height:1.5;text-transform:uppercase}
  .card-front .contact{position:absolute;left:34px;top:116px;font-size:8px}
  .card-front .person{position:absolute;right:26px;top:86px;text-align:right}
  .person-name{font-size:17px;font-weight:600;letter-spacing:.06em;color:var(--ink)}
  .person-role{font-size:8.5px;color:var(--green);letter-spacing:.08em;margin-top:3px}

  .card-back{top:530px;background:linear-gradient(160deg,var(--green-light) 0%,var(--green) 55%,var(--green-dark) 100%)}
  .card-back .decor{position:absolute;right:30px;top:26px;width:120px;height:120px;background:rgba(255,255,255,.18)}
  .card-back .web{position:absolute;left:24px;bottom:20px;font-size:9px;color:var(--white);letter-spacing:.06em}

  /* footer web address */
  .site-url{position:absolute;left:0;right:0;top:832px;text-align:center;font-size:14px;color:var(--white);letter-spacing:.08em}
</style>
</head>
<body>

  <section class="shirt-print" aria-label="T-shirt print">
    <div class="brand">
      <span class="brand-mark"></span>
      <span class="brand-name"><span>Talverne</span><span>Insulation</span></span>
    </div>
  </section>

  <section class="letterhead" aria-label="Letterhead">
    <span class="band lh-band-1"></span>
    <span class="band lh-band-2"></span>
    <span class="band lh-band-3"></span>
    <div class="brand">
      <span class="brand-mark"></span>
      <span class="brand-name"><span>Talverne</span><span>Insulation</span></span>
    </div>
    <dl class="contact">
      <dt>Phone</dt><dd>: (530) 555-0148</dd>
      <dt>Cell</dt><dd>: (530) 555-0162</dd>
      <dt>Fax</dt><dd>: (530) 555-0149</dd>
      <dt>email</dt><dd>: talverneinsulation@mailnest.example</dd>
    </dl>
  </section>

  <section class="envelope" aria-label="Envelope">
    <span class="env-band-top"></span>
    <span class="env-band-top-2"></span>
    <div class="env-decor" role="img" aria-label="Faint large brand square decoration"></div>
    <div class="brand">
      <span class="brand-mark"></span>
      <span class="brand-name"><span>Talverne</span><span>Insulation</span></span>
    </div>
    <p class="address">14 Bristlecone Ct. Marrowdale,<br>CA. 95000</p>
    <dl class="contact">
      <dt>Phone</dt><dd>: (530) 555-0148</dd>
      <dt>Cell</dt><dd>: (530) 555-0162</dd>
      <dt>Fax</dt><dd>: (530) 555-0149</dd>
      <dt>email</dt><dd>: talverneinsulation@mailnest.example</dd>
    </dl>
  </section>

  <section class="card card-front" aria-label="Business card front">
    <span class="strip"></span>
    <span class="strip-2"></span>
    <div class="brand">
      <span class="brand-mark"></span>
      <span class="brand-name"><span>Talverne</span><span>Insulation</span></span>
    </div>
    <p class="address">14 Bristlecone Ct. Marrowdale,<br>CA. 95000</p>
    <dl class="contact">
      <dt>Phone</dt><dd>: (530) 555-0148</dd>
      <dt>Cell</dt><dd>: (530) 555-0162</dd>
      <dt>Fax</dt><dd>: (530) 555-0149</dd>
      <dt>email</dt><dd>: talverneinsulation@mailnest.example</dd>
    </dl>
    <div class="person">
      <p class="person-name">ED TALVERNE</p>
      <p class="person-role">OWNER, SALES</p>
    </div>
  </section>

  <section class="card card-back" aria-label="Business card back">
    <div class="decor" role="img" aria-label="Faint large brand square decoration"></div>
    <p class="web">www.talverneinsulation.example</p>
  </section>

  <p class="site-url">www.talverneinsulation.example</p>

</body>
</html>
```